Business Card Design For DJ Company

I'm rebranding my wedding and event dj company. I am looking for a modern, luxury, & fun design to match my new logo and website design. Please see attached logo and new webpage design. Colors should match. Design should flow with logo and website for recognition. I want to attract young adults. I plan on printing metallic finish cards so please keep hat in mind.

Target Market(s)

Millennials

Contact Information for Business Card

Name: Dario Colvento
Company: Cedar Hollow Mix DJ
Services: DJ – Photo Booth – Event Lighting – LED Robot

Website: www.cedarhollowmixdj.example
Email: dario@cedarhollowmixdj.example
Phone: (555)417-9382

Instagram: @chmixdj
Facebook: @chmixdj
Twitter - @chmixdj

Se Habla Español

Font styles to use
Serif
Sans Serif

Colors

Designer to choose colors to be used in the design.

Requirements
Nice to have
• Transparent Gradient background - Image related to weddings

```html
<!DOCTYPE html>
<html lang="en">
<head>
<meta charset="utf-8">
<title>Cedar Hollow Mix DJ – Business Card</title>
<link href="https://fonts.googleapis.com/css2?family=Lato:wght@400;700&family=Michroma&display=swap" rel="stylesheet">
<style>
  :root {
    --stage: #2e2e2e;
    --paper: #ffffff;
    --orange: #f39422;
    --green: #8cc63f;
    --blue: #29a9e0;
    --ink: #444444;
    --rule: #b5b5b5;
    --white: #ffffff;
  }
  html, body { margin: 0; padding: 0; overflow: hidden; }
  body {
    width: 1200px; height: 1200px;
    background: var(--stage);
    position: relative;
    font-family: "Lato", sans-serif;
  }
  .card {
    position: absolute;
    top: 310px;
    width: 364px; height: 594px;
    box-shadow: 0 4px 12px rgba(0,0,0,0.5);
    overflow: hidden;
  }
  .card--front { left: 234px; background: var(--paper); }
  .card--back {
    left: 627px; width: 369px;
    background: linear-gradient(135deg, var(--orange) 0%, #d9a22c 45%, var(--orange) 70%, var(--green) 100%);
  }

  .brand-mark {
    position: absolute; left: 0; right: 0;
    display: flex; flex-direction: column; align-items: center;
  }
  .card--front .brand-mark { top: 112px; }
  .card--back .brand-mark { top: 172px; }
  .brand-mark__ring {
    width: 150px; height: 150px; border-radius: 50%;
    box-sizing: border-box;
  }
  .card--front .brand-mark__ring { border: 6px solid var(--blue); }
  .card--back .brand-mark__ring { border: 6px solid var(--white); }
  .brand-mark__name {
    margin-top: 14px;
    font-weight: 700; font-size: 20px; letter-spacing: 2px;
    text-align: center; line-height: 1.15;
  }
  .card--front .brand-mark__name { color: var(--orange); }
  .card--back .brand-mark__name { color: var(--white); }

  .holder {
    position: absolute; top: 372px; left: 0; right: 0; text-align: center;
  }
  .holder__name {
    font-family: "Michroma", sans-serif;
    font-size: 16px; letter-spacing: 0.5px; margin: 0;
  }
  .holder__first { color: var(--orange); }
  .holder__last { color: var(--green); }
  .holder__title { font-size: 17px; color: var(--ink); margin: 2px 0 0; }

  .divider {
    position: absolute; left: 79px; right: 79px;
    display: flex; align-items: center; gap: 4px;
  }
  .divider::before, .divider::after {
    content: ""; flex: 1; height: 1px; background: var(--rule);
  }
  .divider--contact { top: 426px; }
  .divider--social { top: 526px; }
  .divider svg { display: block; }

  .contact {
    position: absolute; top: 451px; left: 0; right: 0;
    text-align: center; color: var(--ink); font-size: 17px; line-height: 21.5px;
  }
  .contact p { margin: 0; }
  .handle {
    position: absolute; top: 546px; left: 0; right: 0;
    text-align: center; color: var(--ink); font-size: 17px;
  }

  .palm-decor { position: absolute; inset: 0; }

  .services {
    position: absolute; top: 428px; left: 0; right: 0;
    list-style: none; margin: 0; padding: 0;
    text-align: center; color: var(--white);
    font-size: 20px; line-height: 31px;
  }
</style>
</head>
<body>

  <section class="card card--front">
    <div class="brand-mark">
      <div class="brand-mark__ring"></div>
      <div class="brand-mark__name">CEDAR HOLLOW<br>MIX DJ</div>
    </div>

    <div class="holder">
      <h1 class="holder__name"><span class="holder__first">DARIO</span> <span class="holder__last">COLVENTO</span></h1>
      <p class="holder__title">Managing Director</p>
    </div>

    <div class="divider divider--contact">
      <svg width="64" height="18" viewBox="0 0 64 18" aria-hidden="true">
        <g fill="none" stroke="var(--blue)" stroke-width="1.5">
          <circle cx="9" cy="9" r="8"/>
          <circle cx="32" cy="9" r="8"/>
          <circle cx="55" cy="9" r="8"/>
        </g>
        <path d="M6 5.5c0 4 3 7 6.5 7l1-1.8-2-1-1 1c-1-.5-2-1.5-2.5-2.5l1-1-1-2z" fill="var(--blue)"/>
        <g fill="none" stroke="var(--blue)" stroke-width="1.1">
          <circle cx="32" cy="9" r="4.5"/>
          <ellipse cx="32" cy="9" rx="2" ry="4.5"/>
          <line x1="27.5" y1="9" x2="36.5" y2="9"/>
        </g>
        <rect x="50.5" y="6" width="9" height="6" fill="var(--blue)"/>
        <path d="M50.5 6l4.5 3.5L59.5 6" fill="none" stroke="#fff" stroke-width="1"/>
      </svg>
    </div>

    <div class="contact">
      <p>(555)417-9382</p>
      <p>www.cedarhollowmixdj.example</p>
      <p>dario@cedarhollowmixdj.example</p>
    </div>

    <div class="divider divider--social">
      <svg width="64" height="18" viewBox="0 0 64 18" aria-hidden="true">
        <g fill="var(--green)">
          <circle cx="9" cy="9" r="9"/>
          <circle cx="32" cy="9" r="9"/>
          <circle cx="55" cy="9" r="9"/>
        </g>
      </svg>
    </div>
    <p class="handle">@chmixdj</p>
  </section>

  <section class="card card--back">
    <svg class="palm-decor" width="369" height="594" viewBox="0 0 369 594" role="img" aria-label="Large palm tree silhouette in soft green and orange tones behind the brand mark">
      <defs>
        <linearGradient id="palmTone" x1="0" y1="0" x2="1" y2="1">
          <stop offset="0" stop-color="#a8c23a" stop-opacity="0.75"/>
          <stop offset="1" stop-color="#c6b13a" stop-opacity="0.55"/>
        </linearGradient>
      </defs>
      <rect x="0" y="30" width="369" height="564" fill="url(#palmTone)" opacity="0.35"/>
    </svg>

    <div class="brand-mark">
      <div class="brand-mark__ring"></div>
      <div class="brand-mark__name">CEDAR HOLLOW<br>MIX DJ</div>
    </div>

    <ul class="services">
      <li>DJ</li>
      <li>PHOTO BOOTH</li>
      <li>EVENT LIGHTING</li>
      <li>LED ROBOT</li>
    </ul>
  </section>

</body>
</html>
```